Drone service provider needs a brilliant web design

I need a responsive web design for a new drone service company. Ridgefall Drone Solutions provides turnkey solutions to capture, process, and deliver actionable aerial data to customers. The design should communicate a professional company that is safe, legal and insured. I included our logo design and business card designs for reference.
*content to be supplied after design selected

Target Market(s)

We serve telecommunications, construction, government, utility infrastructure, insurance and other industries.

Industry/Entity Type

Industrial

Number of Pages Required

5+ page

Colors

Designer to choose colors to be used in the design.

Requirements
Must have
• The design should highlight professional services to include Inspections, Mapping, Consulting and Training. The site should include aerial images and video to compliment the services offered. The landing page must include following sections in order: HOME, SERVICES, ABOUT, DEMO REEL, CLIENTS, CONTACT FORM, and social media buttons (Facebook, LinkedIn, Twitter, YouTube, Instagram). Contact: 615-384-2916 info@ridgefalldronesolutions.example Smyrna, TN
• Sitemap:
• 6 pages: Home, Inspections, Mapping, Training, Consulting, About
• HOME (Landing Page)
• • Header with logo and tab links (Home, Services, About, Contact)
• • 'CAPTURE. PROCESS. DELIVER.' tagline and 'CONTACT US' button displayed within aerial image of drone over city or construction site
• • Services section with icons, text and read more link to page
• • About section with photo and text with three icons for SAFE. LEGAL. INSURED.
• • Demo reel
• • Clients logos shown scrolling horizontally
• • Contact form
• • Footer with logo, phone, email, social media buttons
• SERVICES (4 different pages)
• • Inspections
• • Mapping
• • Consulting
• • Training
• ABOUT page
• • Company
• • Partners
• • Certifications & Associations
• • Careers
• CONTACT linked to bottom of landing page
• Would you like to receive the newsletter? Yes or No Drop-down list
Nice to have
• Photos of KVT Wraithwing or Halyard inspecting infrastructure, buildings, construction sites, etc. A photo of one or two pilots in vest and helmet. Free stock photos preferred but would purchase the right photo that's more relevant.
• website references:
• https://www.rotorglimpse.example/
• https://www.pelmarkworks.example/services
• https://www.torvane.example/
• http://loftmetrica.example/
• http://cirrusmark.example/
• http://hoverquill.example/
• https://www.brisk.example/
Should not have
• not an aerial photography or videography service business, no blog or newsletter

```html
<!DOCTYPE html>
<html lang="en">
<head>
<meta charset="utf-8">
<title>Inspections – Ridgefall Drone Solutions</title>
<link rel="stylesheet" href="https://fonts.googleapis.com/css2?family=Montserrat:wght@700;800&family=Open+Sans:wght@400;600;700&display=swap">
<style>
  :root{
    --brand:#1b8fd2;
    --brand-dark:#1573ad;
    --ink:#2b2b2b;
    --muted:#7a7a7a;
    --paper:#ffffff;
    --footer:#262626;
    --footer-line:#4a4a4a;
  }
  *{box-sizing:border-box;margin:0;padding:0}
  html,body{width:1200px;height:2692px;overflow:hidden;background:var(--paper)}
  body{position:relative;font-family:"Open Sans",Arial,sans-serif;color:var(--ink)}
  .abs{position:absolute}

  /* header */
  .topbar{left:0;top:0;width:1200px;height:120px;background:var(--brand)}
  .nav{left:100px;top:48px;display:flex;gap:44px}
  .nav a{color:#fff;text-decoration:none;font-size:17px;font-weight:600;letter-spacing:.5px}
  .logo-tab{left:460px;top:0;width:280px;height:150px}
  .logo{left:460px;top:22px;width:280px;text-align:center;font-family:"Montserrat",Arial,sans-serif;font-weight:800;color:#1d1d1d;line-height:1}
  .logo .big{display:block;font-size:40px;letter-spacing:1px}
  .logo .small{display:block;font-size:13px;letter-spacing:3px;margin-top:6px}
  .social{display:flex;gap:10px}
  .social span{width:30px;height:30px;border:2px solid #fff;border-radius:50%;display:block}
  .social.head{left:920px;top:45px}

  /* hero */
  .hero{left:0;top:120px;width:1200px;height:284px;background:linear-gradient(180deg,#5d6b78 0%,#8a97a3 45%,#4a5560 100%)}
  .hero-title{left:100px;top:254px;color:#fff;font-family:"Montserrat",Arial,sans-serif;font-weight:800;font-size:56px;letter-spacing:1px}

  /* intro */
  .section-title{left:0;top:488px;width:1200px;text-align:center;font-family:"Montserrat",Arial,sans-serif;font-weight:700;font-size:30px;color:var(--brand)}
  .title-rule{left:540px;top:534px;width:120px;height:3px;background:var(--brand)}
  .intro{left:130px;top:566px;width:940px;text-align:center;font-size:14px;line-height:22px;color:var(--muted)}

  /* timeline */
  .spine{left:597px;top:640px;width:6px;height:1450px;background:var(--brand)}
  .photo{width:360px;height:272px}
  .item{display:flex;align-items:flex-start;gap:14px;width:300px;font-size:16px;line-height:24px;color:var(--ink);font-weight:600}
  .item i{flex:none;width:14px;height:14px;border:2px solid var(--brand);border-radius:50%;margin-top:5px}

  .btn{left:522px;top:2146px;width:156px;height:56px;background:var(--brand);color:#fff;font-weight:700;font-size:17px;display:flex;align-items:center;justify-content:center;letter-spacing:.5px;text-decoration:none}

  /* footer */
  .footer{left:0;top:2280px;width:1200px;height:412px;background:var(--footer);color:#fff}
  .footer .logo{color:#fff;top:80px}
  .contact{left:0;top:190px;width:1200px;display:flex;justify-content:center;gap:60px;font-size:20px}
  .contact div{display:flex;align-items:center;gap:14px}
  .ic{width:40px;height:40px;border:2px solid #fff;border-radius:50%;display:flex;align-items:center;justify-content:center}
  .fnav{left:0;top:276px;width:1200px;display:flex;justify-content:center;font-size:16px;font-weight:600}
  .fnav a{color:#fff;text-decoration:none;padding:0 60px;border-left:2px solid #fff;line-height:18px}
  .fnav a:first-child{border-left:none}
  .frule{left:100px;top:324px;width:1000px;height:1px;background:var(--footer-line)}
  .copy{left:100px;top:360px;font-size:14px}
  .social.foot{left:918px;top:352px}
</style>
</head>
<body>

<header>
  <div class="abs topbar"></div>
  <nav class="abs nav"><a href="#">HOME</a><a href="#">SERVICES</a><a href="#">ABOUT</a></nav>
  <svg class="abs logo-tab" viewBox="0 0 280 150"><path d="M0 0 H280 V110 Q140 175 0 110 Z" fill="#fff"/></svg>
  <div class="abs logo"><span class="big">RIDGEFALL</span><span class="small">DRONE SOLUTIONS</span></div>
  <div class="abs social head"><span></span><span></span><span></span><span></span><span></span></div>
</header>

<section>
  <div class="abs hero" role="img" aria-label="Drone flying over a harbour city skyline"></div>
  <h1 class="abs hero-title">INSPECTIONS</h1>
</section>

<main>
  <h2 class="abs section-title">INSPECTIONS</h2>
  <div class="abs title-rule"></div>
  <p class="abs intro">Our certified pilots deliver safe, precise aerial inspections of critical assets, capturing detailed data that helps teams spot issues early, plan repairs and reduce downtime across every site we serve today.</p>

  <div class="abs spine"></div>
  <svg class="abs" style="left:0;top:0" width="1200" height="2100" aria-hidden="true">
    <polygon points="597,728 575,740 597,752" fill="var(--brand)"/>
    <polygon points="603,1016 625,1028 603,1040" fill="var(--brand)"/>
    <polygon points="597,1290 575,1302 597,1314" fill="var(--brand)"/>
    <polygon points="603,1540 625,1552 603,1564" fill="var(--brand)"/>
    <polygon points="597,1830 575,1842 597,1854" fill="var(--brand)"/>
  </svg>

  <div class="abs photo" style="left:608px;top:672px;background:linear-gradient(180deg,#a9c3da,#7d9a7a 70%,#5f7a4c)" role="img" aria-label="Transmission towers and power lines being inspected by a drone"></div>
  <div class="abs item" style="left:228px;top:800px"><i></i><span>Power Utilities (solar, wind, power plants, power lines)</span></div>

  <div class="abs photo" style="left:228px;top:948px;background:linear-gradient(180deg,#c9ced3,#9aa4ab 60%,#6c7a74)" role="img" aria-label="Drone inspecting a highway bridge"></div>
  <div class="abs item" style="left:620px;top:1090px"><i></i><span>Infrastructure (bridges, dams, railways, roads)</span></div>

  <div class="abs photo" style="left:608px;top:1224px;background:linear-gradient(180deg,#8c9fae,#b8c4cc 55%,#56606a)" role="img" aria-label="Drone flying beside a cellular tower"></div>
  <div class="abs item" style="left:228px;top:1350px"><i></i><span>Cellular Tower</span></div>

  <div class="abs photo" style="left:228px;top:1500px;background:linear-gradient(135deg,#6f7b84,#a3aab0 50%,#5a6b4e)" role="img" aria-label="Aerial view of a house roof"></div>
  <div class="abs item" style="left:620px;top:1626px"><i></i><span>Roof</span></div>

  <div class="abs photo" style="left:608px;top:1780px;background:linear-gradient(180deg,#3f5c79,#6b7f8c 50%,#2f6f8a)" role="img" aria-label="Residential property with pool at dusk"></div>
  <div class="abs item" style="left:228px;top:1900px"><i></i><span>Property</span></div>

  <a class="abs btn" href="#">CONTACT US</a>
</main>

<footer class="abs footer">
  <div class="abs logo"><span class="big">RIDGEFALL</span><span class="small">DRONE SOLUTIONS</span></div>
  <div class="abs contact">
    <div><span class="ic"><svg width="20" height="14" viewBox="0 0 20 14"><rect x="1" y="1" width="18" height="12" fill="none" stroke="#fff" stroke-width="2"/><path d="M1 1 L10 8 L19 1" fill="none" stroke="#fff" stroke-width="2"/></svg></span>info@ridgefalldronesolutions.example</div>
    <div><span class="ic"><svg width="18" height="18" viewBox="0 0 24 24"><path d="M6.6 10.8a15 15 0 0 0 6.6 6.6l2.2-2.2c.3-.3.7-.4 1-.2 1.1.4 2.3.6 3.6.6.6 0 1 .4 1 1V20c0 .6-.4 1-1 1A17 17 0 0 1 3 4c0-.6.4-1 1-1h3.5c.6 0 1 .4 1 1 0 1.3.2 2.5.6 3.6.1.3 0 .7-.2 1z" fill="#fff"/></svg></span>615-384-2916</div>
  </div>
  <nav class="abs fnav"><a href="#">HOME</a><a href="#">SERVICES</a><a href="#">ABOUT</a><a href="#">CONTACT US</a></nav>
  <div class="abs frule"></div>
  <p class="abs copy">Copyright © 2018 Ridgefall Drone Solutions. All Right Reserved</p>
  <div class="abs social foot"><span></span><span></span><span></span><span></span><span></span></div>
</footer>

</body>
</html>
```